Improve design on www.vorntakvagt.dk.

The company provides securitysolutions, primarily guards, doorguards, eventsecurity and night club.

Target Market(s)

Private and business, who needs security.

Industry/Entity Type

Club

Requirements
Must have
• Don't use inline style.
Menus must use UL/LI tags.
Nice to have
• Nice animation maybe, shiny.

```html
<!DOCTYPE html>
<html lang="da">
<head>
<meta charset="utf-8">
<title>Vorntak Vagt – Om os</title>
<link rel="stylesheet" href="https://fonts.googleapis.com/css2?family=Bebas+Neue&family=Libre+Baskerville:ital@1&family=Arimo:wght@400;700&display=swap">
<style>
:root{
  --page:#0b0808;
  --panel:#1d1614;
  --text:#f4f1ef;
  --faint:#4d4745;
  --field:#d3d3d3;
  --field-edge:#eeeeee;
  --footer:#d9d9d9;
  --footer-text:#333;
  --accent:#c7302a;
}
*{margin:0;padding:0;box-sizing:border-box}
html,body{width:1200px;height:1200px;overflow:hidden;background:var(--page);font-family:"Arimo",Arial,sans-serif;color:var(--text)}
.site{position:relative;width:1200px;height:1200px}
.utility{position:absolute;top:11px;right:49px;font-size:13px;list-style:none;display:flex;gap:8px}
.utility a{color:var(--text);text-decoration:none}
.panel{position:absolute;left:42px;top:35px;width:1126px;height:1130px;background:var(--panel);overflow:hidden}
.hero-photo{position:absolute;left:0;top:0;width:1126px;height:500px;
  background:radial-gradient(ellipse at 12% 20%,#7a1a14 0%,transparent 35%),
  radial-gradient(ellipse at 62% 45%,#2c2a2b 0%,#1a1617 45%,transparent 70%),
  linear-gradient(90deg,#2a1a16 0%,#3b2a22 40%,#2a2524 70%,#3b2b22 100%)}
.hero-photo::after{content:"";position:absolute;inset:0;background:linear-gradient(180deg,transparent 55%,var(--panel) 100%)}
.brand{position:absolute;left:123px;top:48px;display:flex;align-items:center;gap:8px;text-decoration:none}
.brand-mark{width:58px;height:58px;background:var(--accent)}
.brand-name{font-weight:700;font-size:24px;color:var(--text)}
.main-nav{position:absolute;left:395px;top:92px;list-style:none;display:flex}
.main-nav li a{display:block;padding:9px 9px 0;height:50px;font-size:15px;color:var(--text);text-decoration:none}
.main-nav li.active a{background:#ececec;color:#111;border-radius:3px;padding:9px 12px 0;position:relative;overflow:hidden}
.main-nav li.active a::after{content:"";position:absolute;top:0;left:-60%;width:40%;height:100%;
  background:linear-gradient(90deg,transparent,rgba(255,255,255,.9),transparent);animation:shine 3s infinite}
@keyframes shine{0%{left:-60%}60%,100%{left:130%}}
.headline{position:absolute;left:130px;top:283px;font-family:"Bebas Neue",sans-serif;font-weight:400;font-size:60px;line-height:55px;letter-spacing:2px;color:#fff}
.crumb{position:absolute;left:128px;top:421px;font-family:"Libre Baskerville",serif;font-style:italic;font-size:11px}
.section-title{font-family:"Libre Baskerville",serif;font-style:italic;font-weight:400;font-size:18px;line-height:24px;color:var(--text)}
.about{position:absolute;left:130px;top:485px;width:672px}
.about p{font-size:12.5px;line-height:14.4px;margin:0 0 14.4px 2px}
.about .lead{margin-top:40px}
.faint-brand{display:flex;align-items:center;gap:6px;margin:14px 0 35px 2px}
.faint-brand .sq{width:54px;height:54px;background:var(--faint)}
.faint-brand span{font-weight:700;font-size:26px;color:var(--faint)}
.offer{position:absolute;left:843px;top:527px;width:265px}
.offer .section-title{margin-left:2px}
.offer p{font-size:12.5px;line-height:14.4px;margin-top:21px}
.offer .note{margin-top:14.4px}
.quote-form{margin-top:24px}
.quote-form label{display:block;font-size:12.5px;margin:0 0 8px 12px}
.quote-form input,.quote-form textarea{display:block;width:223px;height:26px;margin:0 0 16px 9px;background:var(--field);border:1px solid var(--field-edge);border-radius:4px}
.quote-form textarea{height:106px;margin-left:10px;resize:none}
.actions{display:flex;gap:28px;margin:12px 0 0 143px}
.actions button{background:none;border:0;color:#555;font:12.5px "Arimo",Arial,sans-serif}
.footer{position:absolute;left:0;top:1165px;width:1200px;height:35px;background:var(--footer);color:var(--footer-text);font-size:11px;letter-spacing:.3px}
.footer ul{position:absolute;left:140px;top:12px;list-style:none;display:flex;gap:18px}
.footer a{color:var(--footer-text);text-decoration:none}
.footer .copy{position:absolute;right:114px;top:12px}
</style>
</head>
<body>
<div class="site">
  <ul class="utility"><li><a href="#">faq</a></li><li>|</li><li><a href="#">login</a></li></ul>
  <div class="panel">
    <div class="hero-photo" role="img" aria-label="Vagt i sort t-shirt med påskriften security i en mørk natklub med rødt lys"></div>
  </div>
  <a class="brand" href="#"><span class="brand-mark"></span><span class="brand-name">VORNTAK VAGT</span></a>
  <ul class="main-nav">
    <li class="active"><a href="#">Om os</a></li>
    <li><a href="#">Vagtydelser</a></li>
    <li><a href="#">Kontakt</a></li>
    <li><a href="#">Afdelinger</a></li>
    <li><a href="#">Login Ansatte</a></li>
    <li><a href="#">Login Ledere</a></li>
    <li><a href="#">Jobs</a></li>
    <li><a href="#">Franchisetager</a></li>
  </ul>
  <h1 class="headline">YOUR SECURITY<br>IS OUR JOB</h1>
  <p class="crumb">» Om os</p>

  <section class="about">
    <h2 class="section-title">Know about our company,<br>Virksomhedsprofil:</h2>
    <p class="lead">Vorntak Vagt er et netværk af lokale vagt- og dørmandsvirksomheder i Danmark. Selskabet bag netværket ejer selv nogle afdelinger, imens resten fungerer som franchise-afdelinger, 100 % ejet af personerne bag afdelingen. Har du interesse i at få dit eget vagt- og/eller dørmandsfirma i Vorntak Vagt ? Så klik her...</p>
    <div class="faint-brand"><span class="sq"></span><span>VORNTAK VAGT</span></div>
    <p>Vorntak Vagt adskiller sig fra andre vagtvirksomheder, ved vores fleksibilitet, serviceniveau og loyalitet overfor gældende lovgivning.</p>
    <p>Hver afdeling har sin egen side her på sitet. Denne finder du under fanebladet "Afdelinger". Her kan du læse om afdelingen, hvad der tilbydes, og finde kontaktinformation.</p>
    <p>Du kan også kontakte os direkte ved at bruge formularen i venstre side - din henvendelse vil så blive videresendt til den relevante afdeling.</p>
    <p>Vorntak Vagt blev grundlagt i foråret 2006. Vort mål var dengang at levere professionelle dørmands- og sikkerhedsvagtløsninger. Vi har siden starten mærket stigende efterspørgsel på vores ydelser, og er nu førende indenfor dette, flere steder i landet.</p>
    <p>De ledende kræfter i Vorntak Vagt, har til sammen over 20 års erfaring i branchen, både i ind- og udland.</p>
    <p>Vorntak Vagt er et firma hvor god holdning og moral, er en selvfølge.<br>Vi arbejder altid på at give kunden den bedst mulige service, vi tror på det gode samarbejde, og hos os er kunden altid i fokus.</p>
    <p>Vorntak Vagt tilbyder vore kunder, præcist det de efterspørger, vi skræddersyr hver enkelt opgave, stor som lille så den passer perfekt til dig og dit sted.<br>vi specialuddanner gerne folk, så du bedre kan udnytte deres tid, hos dig.</p>
    <p>Vores slogan er derfor også vores fremgangsmåde: Vorntak Vagt er til for din sikkerhed.</p>
    <p>Vorntak Vagts personale:<br>Vorntak Vagts ansatte er alle godkendt efter gældende regler, og godkendt af Rigspolitiet som de skal være.<br>Vi forlanger ren straffeattest og et godt personligt ry som en selvfølge.</p>
  </section>

  <aside class="offer">
    <h2 class="section-title">Få et tilbud eller en<br>Dørmand / Vagt på prøve</h2>
    <p>Udfyldelse af denne formular giver dig mulighed for at indhente et tilbud på en ydelse, eller evt. få en vagt gratis på prøve. Din henvendelse vil blive videresendt til den afdeling som er nærmest dig.</p>
    <p class="note">(ikke til forespørgsler om ansættelse: vil du søge ansættelse, skal du istedet kontakte den relevante afdeling direkte pr. mail, post eller telefon)</p>
    <form class="quote-form">
      <label for="navn">Navn</label><input id="navn" type="text">
      <label for="email">Email</label><input id="email" type="email">
      <label for="tlf">Telefon</label><input id="tlf" type="tel">
      <label for="vedr">Vedr.</label><textarea id="vedr"></textarea>
      <div class="actions"><button type="button">send</button><button type="reset">reset</button></div>
    </form>
  </aside>

  <footer class="footer">
    <ul>
      <li><a href="#">Kontakt</a></li>
      <li><a href="#">Login Ansatte</a></li>
      <li><a href="#">Login Ledere</a></li>
      <li><a href="#">Jobs</a></li>
    </ul>
    <p class="copy">© 2011 Vorntak Vagt ApS.&nbsp; Tlf: 4410 2288. All rights reserved.</p>
  </footer>
</div>
</body>
</html>
```